Kestrelguard Letterhead and Template Design

We are looking to freshen up and modernise our business letter heads and cover pages for our documents. Looking at a suit of new designs. I would like a design for:
- Letter Head
- Page 2 follower (for lengthy documents) - fancy
- Page 2 follower (for lengthy documents) - simple version
- Cover Page for reports to sent to client
- Cover Page for internal documents.

Our website is www.kestrelguard-example.com.au.

I have attached a copy of our current brochure for inspiration and our old letter head so you can see what we currently use.

On our Client Cover Page and letter head we would like to include out business awards. Happy for you to change these designs if you have something that would look better. Have also included logos and awards. We won the Coastal Vermin Controller Prize in 2022/23 and also in 2019/2020. We were a state finalist in the Orvane Enterprise Honours this year logo attached.

We like the emblem to be watermarked into the page in the background.

We want something fresh/clean/modern and classy.

Letter head needs to include our Phone Number: 1300555019
Email: hello@kestrelguard-example.com.au
Text: 0400555382
Website: www.kestrelguard-example.com.au

```html
<!DOCTYPE html>
<html lang="en">
<head>
<meta charset="utf-8">
<title>Kestrelguard Letterhead</title>
<link rel="stylesheet" href="https://fonts.googleapis.com/css2?family=Lato:wght@400;700&display=swap">
<style>
  :root {
    --backdrop: #dcdcdc;
    --paper: #ffffff;
    --brand-green: #76bc43;
    --ink: #3a3a3a;
    --gold-light: #f3e2a6;
    --gold-mid: #d9b862;
    --gold-deep: #b8923a;
  }
  * { box-sizing: border-box; margin: 0; padding: 0; }
  html, body { width: 1200px; height: 947px; overflow: hidden; }
  body { background: var(--backdrop); font-family: "Lato", sans-serif; position: relative; }

  .letterhead {
    position: absolute; left: 364px; top: 179px;
    width: 472px; height: 605px;
    background: var(--paper); overflow: hidden;
  }
  .letterhead__top-rule {
    position: absolute; left: 0; top: 0; width: 100%; height: 3px;
    background: var(--brand-green);
  }
  .brand {
    position: absolute; right: 42px; top: 18px;
    display: flex; align-items: center; gap: 7px;
  }
  .brand__dot {
    width: 14px; height: 14px; border-radius: 50%; background: var(--brand-green);
  }
  .brand__name {
    font-family: "Lato", sans-serif; font-weight: 700;
    font-size: 23px; color: var(--ink); letter-spacing: 0.2px;
  }

  .contact {
    position: absolute; left: 43px; top: 540px;
    list-style: none; font-size: 9px; color: var(--ink); line-height: 11px;
  }
  .contact__item { display: flex; align-items: center; gap: 5px; height: 11px; }
  .contact__icon { width: 8px; height: 8px; flex: none; }

  .awards { position: absolute; left: 0; top: 0; width: 472px; height: 605px; }
</style>
</head>
<body>
  <main class="letterhead">
    <div class="letterhead__top-rule"></div>

    <header class="brand">
      <span class="brand__dot"></span>
      <span class="brand__name">Kestrelguard</span>
    </header>

    <ul class="contact">
      <li class="contact__item">
        <svg class="contact__icon" viewBox="0 0 10 10"><path d="M2 1 L4 1 L4.6 3.2 L3.4 4 Q4.4 5.8 6 6.6 L6.8 5.4 L9 6 L9 8 Q8.6 9 7.6 9 Q1 8.4 1 2.4 Q1 1.4 2 1 Z" fill="var(--brand-green)"/></svg>
        <span>1300555019</span>
      </li>
      <li class="contact__item">
        <svg class="contact__icon" viewBox="0 0 10 10"><rect x="2.5" y="0.5" width="5" height="3" fill="var(--brand-green)"/><rect x="0.5" y="3.5" width="9" height="4" rx="0.8" fill="var(--brand-green)"/><rect x="2.5" y="6.5" width="5" height="3" fill="var(--brand-green)"/></svg>
        <span>0400555382</span>
      </li>
      <li class="contact__item">
        <svg class="contact__icon" viewBox="0 0 10 10"><rect x="0.5" y="2" width="9" height="6.5" fill="var(--brand-green)"/><path d="M0.8 2.3 L5 5.6 L9.2 2.3" fill="none" stroke="#fff" stroke-width="0.9"/></svg>
        <span>hello@kestrelguard-example.com.au</span>
      </li>
      <li class="contact__item">
        <svg class="contact__icon" viewBox="0 0 10 10"><circle cx="5" cy="5" r="4.3" fill="none" stroke="var(--brand-green)" stroke-width="1"/><ellipse cx="5" cy="5" rx="1.9" ry="4.3" fill="none" stroke="var(--brand-green)" stroke-width="0.8"/><path d="M0.7 5 H9.3" stroke="var(--brand-green)" stroke-width="0.8"/></svg>
        <span>www.kestrelguard-example.com.au</span>
      </li>
    </ul>

    <svg class="awards" viewBox="0 0 472 605" aria-hidden="true">
      <defs>
        <linearGradient id="goldBand" x1="0" y1="0" x2="1" y2="1">
          <stop offset="0" stop-color="var(--gold-deep)"/>
          <stop offset="0.45" stop-color="var(--gold-light)"/>
          <stop offset="1" stop-color="var(--gold-mid)"/>
        </linearGradient>
        <radialGradient id="goldSeal" cx="0.4" cy="0.35" r="0.7">
          <stop offset="0" stop-color="var(--gold-light)"/>
          <stop offset="1" stop-color="var(--gold-deep)"/>
        </radialGradient>
      </defs>
      <polygon class="awards__ribbon" points="330,605 386,605 472,517 472,464" fill="url(#goldBand)"/>
      <g class="awards__seal">
        <circle cx="440" cy="526" r="29" fill="url(#goldSeal)"/>
        <circle cx="440" cy="526" r="23" fill="#fff"/>
      </g>
      <g class="awards__seal">
        <circle cx="392" cy="572" r="29" fill="url(#goldSeal)"/>
        <circle cx="392" cy="572" r="23" fill="#fff"/>
      </g>
    </svg>
  </main>
</body>
</html>
```